Search Fund needs a PowerPoint template design

We need a eye-catching and compelling PowerPoint design for a new company based in Chicago called Harrow Ridge Partners. We are search fund with a primary mission to acquire a founder/family/entrepreneur owned businesses (This is similar to a Private Equity firm). Our goal is to offer investors a unique avenue to invest in an attractive business acquisition while providing business owners with an alternative path to exit. We would like the design to reflect crisp and professional nature that many financial firms present. The template should build on the design of the logo including expanding a logical color palette. The presentation will be used to describe facts regarding the firm, financial data and key messaging that we want our investors and potential partners to takeaway.

Target Market(s)

Financial Investors

Industry/Entity Type

Finance

Font styles to use
Serif
Sans Serif

Colors

Designer to choose colors to be used in the design.

Requirements
Must have
• Should include cover page and slide examples. Attractive data displays (graphs, charts, infographics etc.); Compelling cover; fly pages to put in between sections; table of contents page. Needs to have white space to add text.
Should not have
• Do not redesign the logo or change the logo colors. Additional colors should be added to the PowerPoint template

```html
<!DOCTYPE html>
<html lang="en">
<head>
<meta charset="utf-8">
<title>Harrow Ridge Partners – Presentation Template</title>
<link rel="stylesheet" href="https://fonts.googleapis.com/css2?family=Oswald:wght@600&family=Open+Sans:wght@400;700;800&display=swap">
<style>
:root{
  --blue:#1b6fc2;
  --blue-mid:#2c86d8;
  --blue-light:#5aa9eb;
  --navy:#1c3b6c;
  --ink:#2a2f36;
  --grey:#8d939a;
  --grey-light:#d9dbde;
  --stage:#f3f3f3;
  --board:#a9a9a9;
  --white:#ffffff;
}
*{margin:0;padding:0;box-sizing:border-box}
html,body{width:1200px;height:2299px;overflow:hidden}
body{font-family:"Open Sans",Arial,sans-serif;color:var(--ink);background:var(--board);position:relative}
.stage{position:absolute;left:0;top:0;width:1200px;height:805px;background:var(--stage)}
.board{position:absolute;left:0;top:805px;width:1200px;height:1494px;background:var(--board)}
.slide{position:absolute;width:546px;height:307px;background:var(--white);overflow:hidden;box-shadow:0 14px 18px -10px rgba(0,0,0,.45)}
.slide.big{width:700px;height:394px;left:250px;top:205px;box-shadow:0 18px 30px -12px rgba(0,0,0,.35)}
.abs{position:absolute}
.photo{position:absolute;left:0;top:0;width:100%}
.photo.handshake{height:76%;background:linear-gradient(110deg,#e8eef3 0%,#c9d3dc 35%,#22304a 55%,#c8b29a 62%,#1f2c44 72%,#dfe5ea 100%)}
.photo.chess{height:100%;background:linear-gradient(120deg,#244f8e 0%,#1d5fb0 40%,#3a7cc8 60%,#1a4f97 100%)}
.cover-band{position:absolute;left:0;bottom:0;width:100%;height:24%;background:var(--blue);display:flex;align-items:center;justify-content:center;border-top:3px solid var(--white)}
.cover-title{font-family:"Oswald",Arial,sans-serif;font-weight:600;color:var(--white);letter-spacing:.5px;white-space:nowrap}
.brand{font-family:"Open Sans",Arial,sans-serif;font-weight:800;color:var(--blue);letter-spacing:.5px;white-space:nowrap;display:flex;align-items:center;gap:6px}
.heading{position:absolute;left:22px;top:18px;padding-left:12px;border-left:3px solid var(--grey);font-weight:800;font-size:13px;color:var(--blue);letter-spacing:.3px;line-height:22px}
.foot{position:absolute;left:20px;right:14px;bottom:14px;height:14px;display:flex;align-items:center;gap:10px}
.foot .brand{font-size:9px}
.foot .rule{flex:1;height:1px;background:var(--grey-light)}
.foot .page{width:14px;height:14px;background:var(--blue);color:var(--white);font-size:7px;display:flex;align-items:center;justify-content:center}
.small{font-size:6.2px;line-height:8.4px;color:var(--ink)}
.label{font-size:7px;font-weight:700;color:var(--blue)}
.tag{display:inline-block;background:var(--blue);color:var(--white);font-size:6.5px;font-weight:700;padding:2px 6px}
ul.bullets{list-style:none}
ul.bullets li{position:relative;padding-left:12px;margin-bottom:9px;font-size:6.2px;line-height:8.4px}
ul.bullets li::before{content:"";position:absolute;left:0;top:2px;width:5px;height:5px;border-radius:50%;background:var(--blue)}
ul.bullets li.sub{margin-left:22px}
.stat-row{position:absolute;left:22px;display:flex;align-items:center;gap:14px;color:var(--white)}
.stat-row .pct{font-weight:800;font-size:15px;width:40px}
.stat-row .small{color:var(--white);width:120px}
.card{position:absolute;top:120px;width:113px;height:140px;border:1px solid rgba(255,255,255,.9)}
.card .body{position:absolute;top:0;left:0;right:0;bottom:0;background:rgba(27,111,194,.88);padding:40px 7px 0}
.card .body .label{color:var(--white);margin-bottom:4px}
.card .body .small{color:var(--white)}
.card .ico{position:absolute;left:38px;top:-24px;width:36px;height:36px;border-radius:50%;background:var(--grey-light);border:4px solid rgba(255,255,255,.7)}
.info-row{display:flex;gap:16px}
.info-row .small{width:115px}
.board-brand{position:absolute;left:700px;top:2082px;width:390px;justify-content:center;font-size:24px;font-weight:800;color:var(--blue);letter-spacing:1px}
</style>
</head>
<body>

<section class="stage">
  <article class="slide big">
    <div class="photo handshake" role="img" aria-label="Photo of two businessmen shaking hands in an office"></div>
    <div class="brand abs" style="left:0;right:0;top:32px;justify-content:center;font-size:30px">HARROW RIDGE PARTNERS</div>
    <div class="cover-band"><h1 class="cover-title" style="font-size:44px">PRESENTATION TITLE GOES HERE</h1></div>
  </article>
</section>

<section class="board"></section>

<!-- Cover -->
<article class="slide" style="left:35px;top:863px">
  <div class="photo handshake" role="img" aria-label="Photo of two businessmen shaking hands in an office"></div>
  <div class="brand abs" style="left:0;right:0;top:22px;justify-content:center;font-size:22px">HARROW RIDGE PARTNERS</div>
  <div class="cover-band"><h1 class="cover-title" style="font-size:34px">PRESENTATION TITLE GOES HERE</h1></div>
</article>

<!-- Key figures -->
<article class="slide" style="left:619px;top:863px">
  <h2 class="heading">HEADING TWO GOES HERE</h2>
  <ul class="bullets abs" style="left:38px;top:84px;width:200px">
    <li>Lorem Ipsum is simply dummy text of the printing and typesetting industry. Lorem Ipsum has been the industry's standard dummy.</li>
    <li>Lorem Ipsum is simply dummy text of the printing and typesetting industry. Lorem Ipsum has been the industry's standard dummy.</li>
    <li class="sub">Lorem Ipsum is simply dummy text of the printing and typesetting industry.</li>
    <li class="sub">Lorem Ipsum is simply dummy text of the printing.</li>
    <li class="sub">Lorem Ipsum is simply dummy text of the printing and typesetting industry.</li>
    <li>Lorem Ipsum is simply dummy text of the printing and typesetting industry. Lorem Ipsum has been the industry's standard dummy.</li>
  </ul>
  <div class="foot" style="right:300px"><span class="brand">HARROW RIDGE PARTNERS</span><span class="rule"></span></div>
  <div class="abs" style="left:272px;top:0;width:274px;height:307px;background:var(--blue)">
    <div class="stat-row" style="top:58px">
      <svg width="28" height="28" viewBox="0 0 28 28"><circle cx="14" cy="14" r="11" fill="none" stroke="#fff" stroke-width="2"/><path d="M14 7v7l5 3" stroke="#fff" stroke-width="2" fill="none"/></svg>
      <span class="pct">50%</span><p class="small">Lorem Ipsum is simply dummy text of the printing and typesetting industry. Lorem Ipsum has been the industry's standard dummy.</p>
    </div>
    <div class="stat-row" style="top:137px">
      <svg width="28" height="28" viewBox="0 0 28 28"><circle cx="14" cy="14" r="11" fill="none" stroke="#fff" stroke-width="2"/><path d="M14 14V3a11 11 0 0 1 11 11z" fill="#fff"/></svg>
      <span class="pct">70%</span><p class="small">Lorem Ipsum is simply dummy text of the printing and typesetting industry. Lorem Ipsum has been the industry's standard dummy.</p>
    </div>
    <div class="stat-row" style="top:216px">
      <svg width="28" height="28" viewBox="0 0 28 28"><path d="M3 14l7-6 4 3 4-3 7 6-9 8z" fill="#fff"/></svg>
      <span class="pct">90%</span><p class="small">Lorem Ipsum is simply dummy text of the printing and typesetting industry. Lorem Ipsum has been the industry's standard dummy.</p>
    </div>
  </div>
</article>

<!-- Four pillars -->
<article class="slide" style="left:35px;top:1220px">
  <div class="photo chess" role="img" aria-label="Blue-toned photo of a hand moving a chess piece"></div>
  <div class="card" style="left:21px"><div class="body"><p class="label">LOREM IPSUM</p><p class="small">Lorem Ipsum is simply dummy text of the printing and typesetting industry. Lorem Ipsum has been the industry's standard dummy. Ipsum is simply dummy text of the printing and typesetting industry.</p></div><span class="ico"></span></div>
  <div class="card" style="left:150px"><div class="body"><p class="label">LOREM IPSUM</p><p class="small">Lorem Ipsum is simply dummy text of the printing and typesetting industry. Lorem Ipsum has been the industry's standard dummy. Ipsum is simply dummy text of the printing and typesetting industry.</p></div><span class="ico"></span></div>
  <div class="card" style="left:280px"><div class="body"><p class="label">LOREM IPSUM</p><p class="small">Lorem Ipsum is simply dummy text of the printing and typesetting industry. Lorem Ipsum has been the industry's standard dummy. Ipsum is simply dummy text of the printing and typesetting industry.</p></div><span class="ico"></span></div>
  <div class="card" style="left:409px"><div class="body"><p class="label">LOREM IPSUM</p><p class="small">Lorem Ipsum is simply dummy text of the printing and typesetting industry. Lorem Ipsum has been the industry's standard dummy. Ipsum is simply dummy text of the printing and typesetting industry.</p></div><span class="ico"></span></div>
</article>

<!-- Progress -->
<article class="slide" style="left:619px;top:1220px">
  <h2 class="heading">HEADING THREE GOES HERE</h2>
  <div class="abs" style="left:36px;top:70px;width:170px">
    <div class="info-row" style="margin-bottom:36px"><svg width="22" height="22" viewBox="0 0 22 22"><circle cx="11" cy="11" r="9" fill="none" stroke="#555" stroke-width="1.5"/><path d="M11 5v6l4 2" stroke="#555" stroke-width="1.5" fill="none"/></svg><div><p class="label">LOREM IPSUM</p><p class="small">Lorem Ipsum is simply dummy text of the printing and typesetting industry.</p></div></div>
    <div class="info-row" style="margin-bottom:36px"><svg width="22" height="22" viewBox="0 0 22 22"><circle cx="11" cy="11" r="9" fill="none" stroke="#555" stroke-width="1.5"/><path d="M11 11V2a9 9 0 0 1 9 9z" fill="#999"/></svg><div><p class="label">LOREM IPSUM</p><p class="small">Lorem Ipsum is simply dummy text of the printing and typesetting industry.</p></div></div>
    <div class="info-row"><svg width="22" height="22" viewBox="0 0 22 22"><path d="M2 11l6-5 3 2 3-2 6 5-8 7z" fill="#888"/></svg><div><p class="label">LOREM IPSUM</p><p class="small">Lorem Ipsum is simply dummy text of the printing and typesetting industry.</p></div></div>
  </div>
  <span class="abs" style="left:215px;top:70px;width:1px;height:175px;background:var(--grey-light)"></span>
  <svg class="abs" style="left:250px;top:62px" width="280" height="60" viewBox="0 0 280 60">
    <g font-family="Open Sans,Arial,sans-serif" font-size="10" font-weight="700" fill="#333" text-anchor="middle">
      <circle cx="40" cy="28" r="18" fill="none" stroke="#ddd" stroke-width="6"/><circle cx="40" cy="28" r="18" fill="none" stroke="#9a9a9a" stroke-width="6" stroke-dasharray="79 113" transform="rotate(-90 40 28)"/><text x="40" y="32">70%</text>
      <circle cx="140" cy="28" r="18" fill="none" stroke="#ddd" stroke-width="6"/><circle cx="140" cy="28" r="18" fill="none" stroke="#9a9a9a" stroke-width="6" stroke-dasharray="68 113" transform="rotate(-90 140 28)"/><text x="140" y="32">60%</text>
      <circle cx="240" cy="28" r="18" fill="none" stroke="#ddd" stroke-width="6"/><circle cx="240" cy="28" r="18" fill="none" stroke="#9a9a9a" stroke-width="6" stroke-dasharray="85 113" transform="rotate(-90 240 28)"/><text x="240" y="32">75%</text>
    </g>
  </svg>
  <p class="small abs" style="left:255px;top:130px;width:270px;text-align:center;font-style:italic">Lorem Ipsum is simply dummy text of the printing and typesetting industry. Lorem Ipsum has been the industry's standard dummy.</p>
  <div class="abs" style="left:262px;top:162px;width:248px">
    <div style="display:flex;align-items:center;gap:6px;margin-bottom:15px"><svg width="9" height="9" viewBox="0 0 10 10"><circle cx="5" cy="5" r="4.3" fill="none" stroke="var(--blue)"/><path d="M3 5l1.5 1.5L7 3.5" stroke="var(--blue)" fill="none"/></svg><div style="flex:1"><p class="label">LOREM IPSUM</p><p class="small">Lorem Ipsum is simply dummy text of the printing.</p></div><svg width="18" height="18" viewBox="0 0 18 18"><circle cx="9" cy="9" r="7" fill="none" stroke="var(--blue)" stroke-width="1.5"/><path d="M9 4v5l3 2" stroke="var(--blue)" stroke-width="1.5" fill="none"/></svg></div>
    <div style="display:flex;align-items:center;gap:6px;margin-bottom:15px"><svg width="9" height="9" viewBox="0 0 10 10"><circle cx="5" cy="5" r="4.3" fill="none" stroke="var(--blue)"/><path d="M3 5l1.5 1.5L7 3.5" stroke="var(--blue)" fill="none"/></svg><div style="flex:1"><p class="label">LOREM IPSUM</p><p class="small">Lorem Ipsum is simply dummy text of the printing.</p></div><svg width="18" height="18" viewBox="0 0 18 18"><circle cx="9" cy="9" r="7" fill="none" stroke="var(--blue)" stroke-width="1.5"/><path d="M9 9V2a7 7 0 0 1 7 7z" fill="var(--blue)"/></svg></div>
    <div style="display:flex;align-items:center;gap:6px"><svg width="9" height="9" viewBox="0 0 10 10"><circle cx="5" cy="5" r="4.3" fill="none" stroke="var(--blue)"/><path d="M3 5l1.5 1.5L7 3.5" stroke="var(--blue)" fill="none"/></svg><div style="flex:1"><p class="label">LOREM IPSUM</p><p class="small">Lorem Ipsum is simply dummy text of the printing.</p></div><svg width="18" height="18" viewBox="0 0 18 18"><path d="M1 9l5-4 3 2 3-2 5 4-8 6z" fill="var(--blue)"/></svg></div>
  </div>
  <div class="foot"><span class="brand">HARROW RIDGE PARTNERS</span><span class="rule"></span><span class="page">4</span></div>
</article>

<!-- Process gears -->
<article class="slide" style="left:35px;top:1571px">
  <h2 class="heading">HEADING THREE GOES HERE</h2>
  <svg class="abs" style="left:0;top:0" width="546" height="307" viewBox="0 0 546 307" font-family="Open Sans,Arial,sans-serif" font-size="6.5" text-anchor="middle" fill="#333">
    <path d="M93 212V182h110" fill="none" stroke="#999"/>
    <path d="M305 130v-20h28" fill="none" stroke="#999"/>
    <path d="M390 212h45v-30h26" fill="none" stroke="#999"/>
    <g><circle cx="96" cy="176" r="8" fill="#bbb"/><path d="M86 176l6-5 4 3 4-3 6 5-10 7z" fill="#777"/></g>
    <circle cx="340" cy="110" r="9" fill="none" stroke="#666" stroke-width="1.5"/><path d="M340 105v5l3 2" stroke="#666" stroke-width="1.5" fill="none"/>
    <circle cx="477" cy="179" r="9" fill="none" stroke="#666" stroke-width="1.5"/><path d="M477 179v-9a9 9 0 0 1 9 9z" fill="#999"/>
    <g><circle cx="255" cy="122" r="38" fill="none" stroke="var(--blue-light)" stroke-width="12" stroke-dasharray="9 7"/><circle cx="255" cy="122" r="36" fill="var(--blue-light)"/><circle cx="255" cy="122" r="26" fill="#fff"/><text x="255" y="124">Text Goes Here</text></g>
    <g><circle cx="227" cy="212" r="28" fill="none" stroke="var(--blue-mid)" stroke-width="10" stroke-dasharray="7 6"/><circle cx="227" cy="212" r="26" fill="var(--blue-mid)"/><circle cx="227" cy="212" r="17" fill="#fff"/><text x="227" y="210">Text Goes</text><text x="227" y="218">Here</text></g>
    <g><circle cx="302" cy="218" r="40" fill="none" stroke="var(--navy)" stroke-width="12" stroke-dasharray="9 7"/><circle cx="302" cy="218" r="38" fill="var(--navy)"/><circle cx="302" cy="218" r="26" fill="#fff"/><text x="302" y="220">Text Goes Here</text></g>
    <g><circle cx="390" cy="224" r="42" fill="none" stroke="#1a2636" stroke-width="12" stroke-dasharray="9 7"/><circle cx="390" cy="224" r="40" fill="#1a2636"/><circle cx="390" cy="224" r="30" fill="#fff"/><text x="390" y="226">Text Goes Here</text></g>
  </svg>
  <div class="foot"><span class="brand">HARROW RIDGE PARTNERS</span><span class="rule"></span><span class="page">5</span></div>
</article>

<!-- Timeline -->
<article class="slide" style="left:619px;top:1571px">
  <h2 class="heading">HEADING FOUR GOES HERE</h2>
  <svg class="abs" style="left:0;top:0" width="546" height="307" viewBox="0 0 546 307" font-family="Open Sans,Arial,sans-serif" font-size="7" fill="#666" text-anchor="middle">
    <line x1="18" y1="164" x2="520" y2="164" stroke="#999" stroke-width="1.5"/><path d="M520 160l8 4-8 4z" fill="#999"/>
    <circle cx="18" cy="164" r="3" fill="#999"/>
    <g stroke="var(--blue)" stroke-width="1"><line x1="32" y1="108" x2="32" y2="164"/><line x1="244" y1="108" x2="244" y2="164"/><line x1="446" y1="108" x2="446" y2="164"/><line x1="138" y1="164" x2="138" y2="219"/><line x1="344" y1="164" x2="344" y2="219"/></g>
    <g fill="var(--blue)"><circle cx="32" cy="164" r="4"/><circle cx="138" cy="164" r="4"/><circle cx="244" cy="164" r="4"/><circle cx="344" cy="164" r="4"/><circle cx="446" cy="164" r="4"/></g>
    <g><circle cx="32" cy="97" r="13" fill="#ddd"/><circle cx="32" cy="97" r="9" fill="var(--blue)"/><text x="32" y="78">2016</text></g>
    <g><circle cx="244" cy="97" r="13" fill="#ddd"/><circle cx="244" cy="97" r="9" fill="var(--blue)"/><text x="244" y="78">2016</text></g>
    <g><circle cx="446" cy="97" r="13" fill="#ddd"/><circle cx="446" cy="97" r="9" fill="var(--blue)"/><text x="446" y="78">2016</text></g>
    <g><circle cx="138" cy="230" r="13" fill="#ddd"/><circle cx="138" cy="230" r="9" fill="var(--blue)"/><text x="138" y="256">2017</text></g>
    <g><circle cx="344" cy="230" r="13" fill="#ddd"/><circle cx="344" cy="230" r="9" fill="var(--blue)"/><text x="344" y="256">2017</text></g>
  </svg>
  <div class="abs" style="left:48px;top:110px"><span class="tag">TEXT HERE</span><p class="small" style="width:50px;margin-top:5px">Lorem Ipsum is simply dummy text of the printing.</p></div>
  <div class="abs" style="left:260px;top:110px"><span class="tag">TEXT HERE</span><p class="small" style="width:50px;margin-top:5px">Lorem Ipsum is simply dummy text of the printing.</p></div>
  <div class="abs" style="left:462px;top:110px"><span class="tag">TEXT HERE</span><p class="small" style="width:50px;margin-top:5px">Lorem Ipsum is simply dummy text of the printing.</p></div>
  <div class="abs" style="left:154px;top:200px"><span class="tag">TEXT HERE</span><p class="small" style="width:50px;margin-top:5px">Lorem Ipsum is simply dummy text of the printing.</p></div>
  <div class="abs" style="left:360px;top:200px"><span class="tag">TEXT HERE</span><p class="small" style="width:50px;margin-top:5px">Lorem Ipsum is simply dummy text of the printing.</p></div>
  <div class="foot"><span class="brand">HARROW RIDGE PARTNERS</span><span class="rule"></span><span class="page">6</span></div>
</article>

<!-- Data charts -->
<article class="slide" style="left:35px;top:1925px">
  <h2 class="heading">HEADING FOUR GOES HERE</h2>
  <p class="small abs" style="left:22px;top:52px;width:500px;font-size:6.6px;line-height:9px">Lorem Ipsum is simply dummy text of the printing and typesetting industry. Lorem Ipsum has been the industry's standard dummy text ever since the 1500s, when an unknown printer took a galley of type and scrambled it to make a type specimen book. It has survived not only five centuries, but also the leap into electronic typesetting, remaining essentially unchanged.</p>
  <svg class="abs" style="left:0;top:0" width="546" height="307" viewBox="0 0 546 307" font-family="Open Sans,Arial,sans-serif" font-size="6" fill="#333">
    <g transform="translate(95 180)">
      <path d="M0 0L-50 -30A58 58 0 0 1 -10 -57z" fill="var(--blue)"/>
      <path d="M0 0L0 -40A40 40 0 0 1 38 -12z" fill="#c9ccd0"/>
      <path d="M0 0L38 -12A40 40 0 0 1 30 26z" fill="#dfe1e4"/>
      <path d="M0 0L30 26A40 40 0 0 1 -10 38z" fill="#b8bcc1"/>
      <path d="M0 0L-10 38A40 40 0 0 1 -38 12z" fill="#d2d5d9"/>
      <path d="M0 0L-38 12A40 40 0 0 1 -34 -20z" fill="#c2c6cb"/>
      <path d="M-55 -18A58 58 0 0 0 20 55" fill="none" stroke="var(--blue-mid)" stroke-width="7"/>
      <path d="M-68 0A68 68 0 0 0 -10 67" fill="none" stroke="var(--blue)" stroke-width="6"/>
      <text x="-24" y="-36" fill="#fff" font-weight="700" font-size="6" text-anchor="middle">Your Title</text>
      <text x="10" y="8">40%</text><text x="-25" y="20">30%</text>
    </g>
    <line x1="160" y1="200" x2="260" y2="200" stroke="#6b7ea8" stroke-dasharray="2 2"/>
    <line x1="210" y1="150" x2="210" y2="252" stroke="#6b7ea8" stroke-dasharray="2 2"/>
    <g transform="translate(210 200)">
      <circle r="26" fill="var(--navy)"/>
      <path d="M0 0V-26A26 26 0 0 1 24 10z" fill="var(--blue)"/>
      <path d="M0 0L24 10A26 26 0 0 1 -6 25z" fill="var(--blue-mid)"/>
      <circle r="26" fill="none" stroke="#fff" stroke-width="1"/>
    </g>
    <g font-size="5" fill="#666"><text x="268" y="152">50%</text><text x="268" y="172">40%</text><text x="268" y="192">30%</text><text x="268" y="212">20%</text><text x="268" y="232">10%</text></g>
    <g>
      <rect x="288" y="150" width="14" height="90" fill="var(--blue)"/><rect x="302" y="150" width="5" height="90" fill="var(--navy)"/>
      <rect x="313" y="180" width="14" height="60" fill="var(--blue)"/><rect x="327" y="180" width="5" height="60" fill="var(--navy)"/>
      <rect x="338" y="200" width="14" height="40" fill="var(--blue)"/><rect x="352" y="200" width="5" height="40" fill="var(--navy)"/>
      <rect x="363" y="190" width="14" height="50" fill="var(--blue)"/><rect x="377" y="190" width="5" height="50" fill="var(--navy)"/>
      <rect x="388" y="205" width="14" height="35" fill="var(--blue)"/><rect x="402" y="205" width="5" height="35" fill="var(--navy)"/>
      <rect x="413" y="155" width="14" height="85" fill="var(--blue)"/><rect x="427" y="155" width="5" height="85" fill="var(--navy)"/>
    </g>
  </svg>
  <div class="foot"><span class="brand">HARROW RIDGE PARTNERS</span><span class="rule"></span><span class="page">7</span></div>
</article>

<div class="brand board-brand">HARROW RIDGE PARTNERS</div>

</body>
</html>
```